Angebotsflyer - nicht Einladung -  für Personalmarketing Agentur
Angebotsflyer - nicht Einladung - für Personalmarketing Agentur
Zielgruppe
Wir sind eine Personalmarketing Agentur, die Unternehmen zu einer starken Arbeitgebermarke verhilft. Achtung: Wir sind keine Personalvermittler. Unternehmen, die als Arbeitgeber sichtbar werden möchten oder die ihre Mitarbeiterzufriedenheit steigern möchten sind unsere Zielgruppe.
Aufgabenstellung
DIN Lang. Wir möchten den Kreativen so viel Gestaltungsraum wie möglich lassen mit der Bitte sich nach unserer Website zu orientieren: www.teamfunke.works
Unser Leistungs-Portfolio sollte ansprechend dargestellt werden:
- Individuelles Recruiting
- Stellenanzeigen
- Mitarbeiterbefragungen
- Was Bewerber wollen
- Karriereseiten
- Mitarbeiter Benefits
- HR digital
- Corporate Fashion
- nUb Akademie (HR Workshops: Personalmarketing, Mitarbeitermotivation und -bindung, Stellenanzeigen, etc.)
nUb steht für never upset balance und für ehrliches Personalmarketing. Dabei ist es essentiell sich zunächst dem internen Personalmarketing zu widmen. Von innen heraus entsteht dann ein stimmiges externes Personalmarketingkonzept, welches von den Mitarbeitern getragen wird.
Gutes Personalmarketing ist mehr als das jährliche Grillfest.

```html
<!DOCTYPE html>
<html lang="de">
<head>
<meta charset="utf-8">
<title>nUb Personalmarketing – Leistungsflyer</title>
<link rel="stylesheet" href="https://fonts.googleapis.com/css2?family=Open+Sans:wght@400;600;700;800&display=swap">
<style>
  :root{
    --petrol:#28505f;
    --petrol-deep:#1d3d4b;
    --ink:#1f4454;
    --teal:#3fc3bf;
    --white:#ffffff;
    --page:#ffffff;
    --photo-a:#0f2233;
    --photo-b:#24405a;
    --photo-c:#3a6f95;
  }
  *{margin:0;padding:0;box-sizing:border-box}
  html,body{width:1113px;height:1200px;overflow:hidden;background:var(--page)}
  body{font-family:"Open Sans",Arial,sans-serif;position:relative}
  .flyer{
    position:absolute;left:148px;top:23px;width:721px;height:1020px;
    transform:scale(1.132);transform-origin:0 0;
    background:var(--petrol);overflow:hidden;
  }
  .hero-photo{position:absolute;inset:0;width:721px;height:400px}
  .logo-box{
    position:absolute;left:57px;top:60px;width:174px;height:131px;background:var(--white);
    display:flex;flex-direction:column;align-items:center;justify-content:center;
    color:var(--ink);font-weight:700;text-align:center;
  }
  .logo-box .brand{font-size:40px;line-height:1}
  .logo-box .brand-sub{font-size:11px;letter-spacing:.5px;margin-top:8px}
  .headline{
    position:absolute;left:33px;top:298px;color:var(--white);
    font-weight:800;font-size:47px;line-height:57px;letter-spacing:-.3px;
  }
  .accent-rule{position:absolute;left:33px;top:431px;width:660px;height:7px;background:var(--teal)}
  .mission{position:absolute;left:33px;top:458px;color:var(--white);font-weight:700;font-size:19.5px}
  .band{position:absolute;left:0;width:721px}
  .band-services{top:510px;height:63px}
  .section-title{position:absolute;left:33px;top:529px;color:var(--ink);font-weight:800;font-size:19.5px}
  .services{position:absolute;left:0;top:596px;width:721px}
  .service{position:absolute;width:170px;text-align:center;color:var(--teal);font-weight:700;font-size:14.5px;line-height:18px}
  .service svg{display:block;margin:0 auto 18px;width:54px;height:54px}
  .divider{position:absolute;width:2px;height:98px;background:var(--teal)}
  .academy{position:absolute;left:33px;top:850px;color:var(--white);font-weight:700;font-size:19px;line-height:27px}
  .band-footer{top:931px;height:89px}
  .contact{position:absolute;display:flex;align-items:center;gap:10px;color:var(--ink);font-weight:700;font-size:12px;line-height:14px}
  .contact svg{width:22px;height:22px;flex:none}
</style>
</head>
<body>
<div class="flyer">
  <svg class="hero-photo" viewBox="0 0 721 400" role="img" aria-label="Foto: Geschäftsmann im Anzug hält schützend die Hände um leuchtende Personensymbole">
    <defs>
      <radialGradient id="glow" cx="0.78" cy="0.5" r="0.55">
        <stop offset="0" stop-color="var(--photo-c)"/>
        <stop offset="0.5" stop-color="var(--photo-b)"/>
        <stop offset="1" stop-color="var(--photo-a)"/>
      </radialGradient>
    </defs>
    <rect width="721" height="400" fill="url(#glow)"/>
  </svg>
  <svg class="band" style="top:0;height:1020px" viewBox="0 0 721 1020" aria-hidden="true">
    <polygon points="0,270 400,270 550,389 721,389 721,1020 0,1020" fill="var(--petrol)"/>
    <polygon points="0,510 370,510 415,546 721,546 721,573 0,573" fill="var(--white)"/>
    <polygon points="0,931 297,931 343,968 721,968 721,1020 0,1020" fill="var(--white)"/>
  </svg>

  <div class="logo-box">
    <div class="brand">nUb</div>
    <div class="brand-sub">PERSONALMARKETING GMBH</div>
  </div>

  <h1 class="headline">Ehrliches<br>Personalmarketing</h1>
  <div class="accent-rule"></div>
  <p class="mission">Ihr Personalmarketing &amp; Employer Branding ist unsere Mission</p>

  <h2 class="section-title">Unsere Leistungen im Überblick</h2>

  <div class="services">
    <div class="service" style="left:6px;top:0">
      <svg viewBox="0 0 54 54" fill="none" stroke="#fff" stroke-width="2"><rect x="4" y="14" width="46" height="34"/><path d="M19 14V7h16v7M4 28h46M23 25h8v6h-8z"/></svg>
      Individuelles<br>Recruiting</div>
    <div class="divider" style="left:163px;top:2px"></div>
    <div class="service" style="left:175px;top:0">
      <svg viewBox="0 0 54 54" fill="none" stroke="#fff" stroke-width="2"><path d="M8 22h10l22-12v34L18 32H8z"/><path d="M13 32l4 14h6l-3-14M45 22h6M45 30h6"/></svg>
      Stellenanzeigen</div>
    <div class="divider" style="left:346px;top:2px"></div>
    <div class="service" style="left:368px;top:0">
      <svg viewBox="0 0 54 54" fill="none" stroke="#fff" stroke-width="2"><rect x="4" y="4" width="46" height="36"/><path d="M12 32V22M22 32V14M32 32V18M42 32V10M18 48h18M27 40v8"/></svg>
      Mitarbeiterbefragungen</div>
    <div class="divider" style="left:554px;top:2px"></div>
    <div class="service" style="left:549px;top:0">
      <svg viewBox="0 0 54 54" fill="none" stroke="#fff" stroke-width="2"><circle cx="27" cy="22" r="19"/><circle cx="27" cy="22" r="12"/><circle cx="27" cy="22" r="4"/><path d="M27 41v9M19 50h16"/></svg>
      Was Bewerber<br>wollen</div>

    <div class="service" style="left:6px;top:140px">
      <svg viewBox="0 0 54 54" fill="none" stroke="#fff" stroke-width="2"><rect x="4" y="4" width="46" height="46"/><path d="M4 12h46M8 8h2M12 8h2M12 20h30M12 27h30M12 34h12M30 34h12M12 41h12M30 41h12"/></svg>
      Karriereseiten</div>
    <div class="divider" style="left:163px;top:125px"></div>
    <div class="service" style="left:175px;top:140px">
      <svg viewBox="0 0 54 54" fill="none" stroke="#fff" stroke-width="2"><path d="M27 48V6M19 14l8-8 8 8M11 48V20M5 26l6-6 6 6M43 48V20M37 26l6-6 6 6M4 48h46"/></svg>
      Mitarbeiter Benefits</div>
    <div class="divider" style="left:346px;top:125px"></div>
    <div class="service" style="left:368px;top:140px">
      <svg viewBox="0 0 54 54" fill="none" stroke="#fff" stroke-width="2"><rect x="17" y="18" width="20" height="20"/><circle cx="27" cy="5" r="3"/><circle cx="5" cy="28" r="3"/><circle cx="49" cy="28" r="3"/><circle cx="27" cy="50" r="3"/><path d="M27 8v10M8 28h9M37 28h9M27 38v9M20 18l-6-8M34 18l6-8"/></svg>
      HR digital</div>
    <div class="divider" style="left:554px;top:125px"></div>
    <div class="service" style="left:549px;top:140px">
      <svg viewBox="0 0 54 54" fill="#fff"><path d="M18 4l9 8 9-8 12 6v40H6V10z"/><path d="M27 12l-3 4 3 22 3-22z" fill="var(--petrol)"/></svg>
      Corporate<br>Fashion</div>
  </div>

  <p class="academy">nUb Akademie (HR Workshops: Personalmarketing,<br>Mitarbeitermotivation und -bindung, Stellenanzeigen, etc.)</p>

  <div class="contact" style="left:33px;top:943px">
    <svg viewBox="0 0 22 22" fill="none" stroke="var(--ink)" stroke-width="1.5"><path d="M11 19s-6-6-6-10a6 6 0 0 1 12 0c0 4-6 10-6 10z"/><circle cx="11" cy="9" r="2"/></svg>
    <span>Mara Kessler Ahornallee 21b<br>28211 Bremen</span>
  </div>
  <div class="contact" style="left:33px;top:985px">
    <svg viewBox="0 0 22 22" fill="none" stroke="var(--ink)" stroke-width="1.5"><path d="M5 3l4 4-2 3c1 2 3 4 5 5l3-2 4 4-3 3C9 19 3 13 2 6z"/></svg>
    <span>Telefon: 0421 98 76 54 32</span>
  </div>
  <div class="contact" style="left:241px;top:985px">
    <svg viewBox="0 0 22 22" fill="none" stroke="var(--ink)" stroke-width="1.5"><rect x="2" y="5" width="18" height="12"/><path d="M2 5l9 7 9-7"/></svg>
    <span>E-Mail: info@nub-team.de</span>
  </div>
  <div class="contact" style="left:456px;top:985px">
    <svg viewBox="0 0 22 22" fill="none" stroke="var(--ink)" stroke-width="1.5"><circle cx="11" cy="11" r="9"/><path d="M2 11h18M11 2c3 3 3 15 0 18M11 2c-3 3-3 15 0 18"/></svg>
    <span>www.teamfunke.works</span>
  </div>
</div>
</body>
</html>
```